BrightLoop Vents Services need a Business Card!

Need a business card designed for a new start company called BrightLoop! I have attached a Zip file (Please let me know if you cannot open this file) with all logos and also a sheets that includes fonts and colors. Last, you will see the design of our vans which will help design the cards too!
The card is needing to be double sided. A place for email, name, headshot, cell #, Office #, Job Title (Head shot optional)

Target Market(s)

People who need their HVAC filters changed. Residential and Commercial

Industry/Entity Type

Hvac Filter Changing Service

Contact Information for Business Card

Website: BrightLoopVents.us Office phone: 517.268.3390 The card is needing to be double sided. A place for email, name, headshot, cell #, Office #, Job Title (Head shot optional)

Requirements
Must have
• Color code and fonts form attached sheets and files

```html
<!DOCTYPE html>
<html lang="en">
<head>
<meta charset="UTF-8">
<title>BrightLoop Vents Services – Business Card</title>
<link rel="stylesheet" href="https://fonts.googleapis.com/css2?family=Montserrat:wght@400;500;600;700&display=swap">
<style>
  :root {
    --navy: #2a2cb4;
    --sky: #3a8dfb;
    --ink: #2325a6;
    --muted: #2d66e6;
    --pattern: #3350e0;
    --backdrop: #ece6d8;
  }
  * { box-sizing: border-box; margin: 0; padding: 0; }
  html, body { width: 1200px; height: 800px; overflow: hidden; }
  body {
    background: var(--backdrop);
    font-family: "Montserrat", sans-serif;
    position: relative;
  }
  .card {
    position: absolute;
    top: 245px;
    width: 540px;
    height: 309px;
    overflow: hidden;
  }

  /* Front side */
  .card--front { left: 40px; background: var(--navy); }
  .edge-pattern {
    position: absolute;
    top: 0;
    width: 60px;
    height: 100%;
    background: linear-gradient(90deg, var(--pattern), rgba(51,80,224,0));
    opacity: .6;
  }
  .edge-pattern--left { left: 0; }
  .edge-pattern--right { right: 0; transform: scaleX(-1); }
  .front-brand {
    position: absolute;
    left: 0; right: 0; top: 58px;
    display: flex;
    flex-direction: column;
    align-items: center;
    gap: 22px;
  }
  .front-brand__mark {
    width: 92px; height: 92px;
    background: var(--sky);
  }
  .front-brand__name {
    color: var(--sky);
    font-weight: 600;
    font-size: 52px;
    line-height: 1;
    letter-spacing: 1px;
  }

  /* Back side */
  .card--back { left: 620px; background: var(--sky); color: var(--ink); }
  .back-brand {
    position: absolute;
    left: 30px; top: 46px;
    display: flex;
    align-items: center;
    gap: 10px;
  }
  .back-brand__mark { width: 26px; height: 26px; background: var(--ink); }
  .back-brand__name { font-weight: 600; font-size: 25px; line-height: 1; }
  .brand-feature {
    position: absolute;
    left: 0; top: 140px;
    width: 250px; height: 150px;
    background: linear-gradient(180deg, rgba(35,37,166,.55), rgba(35,37,166,.25));
  }
  .person {
    position: absolute;
    right: 26px; top: 38px;
    text-align: right;
  }
  .person__name { font-weight: 600; font-size: 24px; letter-spacing: .5px; }
  .person__title {
    font-weight: 500; font-size: 11px; letter-spacing: 1.5px;
    color: var(--muted); margin-top: 3px;
  }
  .contacts {
    position: absolute;
    right: 26px; top: 112px;
    width: 220px;
  }
  .rule { height: 3px; background: var(--ink); border-radius: 2px; }
  .contact {
    display: flex;
    align-items: center;
    justify-content: flex-end;
    gap: 12px;
    height: 48px;
  }
  .contact__text { font-size: 12px; font-weight: 600; text-align: right; line-height: 1.3; }
  .contact__text--web { color: var(--muted); font-weight: 500; }
  .contact__text--small { font-size: 10px; font-weight: 700; }
  .contact__icon { width: 26px; height: 26px; flex: none; }
</style>
</head>
<body>
  <section class="card card--front" aria-label="Business card front">
    <div class="edge-pattern edge-pattern--left" role="img" aria-label="Decorative wind-stroke pattern along the left edge"></div>
    <div class="edge-pattern edge-pattern--right" role="img" aria-label="Decorative wind-stroke pattern along the right edge"></div>
    <div class="front-brand">
      <div class="front-brand__mark" aria-hidden="true"></div>
      <h1 class="front-brand__name">BrightLoop</h1>
    </div>
  </section>

  <section class="card card--back" aria-label="Business card back">
    <div class="back-brand">
      <div class="back-brand__mark" aria-hidden="true"></div>
      <div class="back-brand__name">BrightLoop</div>
    </div>
    <div class="brand-feature" role="img" aria-label="Large brand mark decoration"></div>
    <div class="person">
      <div class="person__name">LOREM IPSUM</div>
      <div class="person__title">LOREM IPSUM DOLOR</div>
    </div>
    <div class="contacts">
      <div class="rule"></div>
      <div class="contact">
        <span class="contact__text">517.268.3390</span>
        <svg class="contact__icon" viewBox="0 0 26 26" aria-hidden="true">
          <circle cx="13" cy="13" r="13" fill="var(--ink)"/>
          <path d="M9 7.5c.6-.5 1.3-.4 1.7.2l1 1.6c.3.5.2 1.1-.2 1.5l-.8.7c.6 1.4 1.7 2.6 3.1 3.3l.7-.8c.4-.4 1-.5 1.5-.2l1.6 1c.6.4.7 1.1.2 1.7l-.8.9c-.6.6-1.5.8-2.3.5-3.2-1.2-5.6-3.7-6.7-6.9-.3-.8-.1-1.7.5-2.3z" fill="var(--sky)"/>
        </svg>
      </div>
      <div class="rule"></div>
      <div class="contact">
        <span class="contact__text contact__text--web">BrightLoopVents.us</span>
        <svg class="contact__icon" viewBox="0 0 26 26" aria-hidden="true">
          <circle cx="13" cy="13" r="13" fill="var(--ink)"/>
          <g fill="none" stroke="var(--sky)" stroke-width="1.4">
            <circle cx="13" cy="13" r="6.5"/>
            <ellipse cx="13" cy="13" rx="2.8" ry="6.5"/>
            <path d="M6.5 13h13"/>
          </g>
        </svg>
      </div>
      <div class="rule"></div>
      <div class="contact">
        <span class="contact__text contact__text--small">218 Maple Ave Ste 400<br>Lakewood, CO 80226</span>
        <svg class="contact__icon" viewBox="0 0 26 26" aria-hidden="true">
          <circle cx="13" cy="13" r="13" fill="var(--ink)"/>
          <path d="M13 6a5 5 0 0 0-5 5c0 3.6 5 9 5 9s5-5.4 5-9a5 5 0 0 0-5-5z" fill="none" stroke="var(--sky)" stroke-width="1.5"/>
          <circle cx="13" cy="11" r="1.8" fill="var(--sky)"/>
        </svg>
      </div>
    </div>
  </section>
</body>
</html>
```